Biz Card for Harrowfield Property Partners - HWPP

Harrowfield Property Partners is a commercial real estate acquisitions firm. We buy commercial property and need to raise capital from investors for each deal we buy. The vibe needs to be: give us your money, we will multiply it.
Our website: www.hrwpp-example.com
Competitors are: https://velmarholdings-example.com/, https://tribanquepartners-example.com/, http://www.ostrellecapital-example.com/
Target Market(s)
High Net Worth Individuals, Bankers, Insurance Companies, Commercial Real Estate Brokers.
Industry/Entity Type
Investment Banking
Contact Information for Business Card
Name, Title, Addess, Cell#, Office#, email, website
Requirements
Must have
- use one of our logos. See website for look and feel: www.hrwpp-example.com
Nice to have
- see website: www.hrwpp-example.com

```html
<!DOCTYPE html>
<html lang="en">
<head>
<meta charset="utf-8">
<title>Harrowfield Property Partners – Stationery</title>
<link href="https://fonts.googleapis.com/css2?family=Lato:wght@400;700&family=Arimo:wght@400;700&display=swap" rel="stylesheet">
<style>
  :root {
    --navy: #0f2740;
    --paper: #f4f4f4;
    --card: #ffffff;
    --ink: #222222;
    --muted: #3a4a5c;
    --rule: #8a96a3;
    --backdrop: #e2e2e2;
  }
  * { margin: 0; padding: 0; box-sizing: border-box; }
  html, body { width: 1200px; height: 960px; overflow: hidden; }
  body { background: var(--backdrop); position: relative; font-family: 'Lato', sans-serif; }

  /* Letterhead */
  .letterhead { position: absolute; left: 142px; top: 84px; width: 613px; height: 791px; background: var(--paper); overflow: hidden; }
  .lh-brand { position: absolute; left: 50px; top: 38px; display: flex; align-items: center; gap: 14px; }
  .brand-dot { display: block; width: 64px; height: 64px; border-radius: 50%; background: var(--navy); flex: none; }
  .brand-name { color: var(--navy); font-weight: 400; line-height: 1; }
  .lh-brand .brand-name .line1 { display: block; font-size: 21px; letter-spacing: 3px; }
  .lh-brand .brand-name .line2 { display: block; font-size: 9.5px; letter-spacing: 2.8px; margin-top: 7px; }

  .lh-contact { position: absolute; left: 454px; top: 40px; right: 0; font-size: 9.5px; color: var(--ink); line-height: 12px; }
  .lh-contact .address { padding-bottom: 5px; border-bottom: 1px solid var(--rule); }
  .lh-contact .channels { padding-top: 4px; }
  .contact-row { display: flex; align-items: center; gap: 4px; }
  .contact-row svg { width: 8px; height: 8px; fill: var(--navy); flex: none; }

  .letter { position: absolute; left: 51px; top: 212px; width: 512px; font-family: 'Arimo', Arial, sans-serif; font-size: 9px; line-height: 12px; color: var(--ink); }
  .letter .date { margin-bottom: 27px; }
  .letter .salutation { font-weight: 700; margin-bottom: 24px; }
  .letter p.body { text-align: justify; margin-bottom: 12px; }
  .letter .closing { margin-top: 36px; }
  .signature { display: block; width: 132px; height: 22px; margin: 12px 0 8px; background: linear-gradient(90deg, #cfd2d6, #e6e7e9); border-radius: 3px; }

  .lh-footer { position: absolute; left: 0; bottom: 0; width: 100%; height: 26px; background: var(--navy); color: #fff; font-size: 9px; letter-spacing: 2.5px; text-align: center; line-height: 26px; }

  /* Business card front */
  .card-front { position: absolute; left: 805px; top: 210px; width: 252px; height: 144px; background: var(--navy); overflow: hidden; }
  .card-front .brand { position: absolute; right: 30px; top: 92px; text-align: center; color: #fff; }
  .card-front .brand .line1 { font-size: 11.5px; letter-spacing: 2px; display: block; }
  .card-front .brand .line2 { font-size: 5.5px; letter-spacing: 1.8px; display: block; margin-top: 3px; }
  .card-front .url { display: block; font-size: 6px; letter-spacing: 1.6px; margin-top: 4px; }

  /* Business card back */
  .card-back { position: absolute; left: 805px; top: 397px; width: 252px; height: 143px; background: var(--card); overflow: hidden; }
  .card-back .brand { position: absolute; left: 12px; top: 18px; width: 100px; text-align: center; color: var(--navy); }
  .card-back .brand-dot { width: 34px; height: 34px; margin: 0 auto 8px; }
  .card-back .brand .line1 { display: block; font-size: 8.5px; letter-spacing: 1.2px; }
  .card-back .brand .line2 { display: block; font-size: 5px; letter-spacing: 1.2px; margin-top: 3px; }
  .card-back .address { position: absolute; left: 18px; top: 112px; font-size: 6px; line-height: 8.5px; color: var(--muted); }
  .card-back .person { position: absolute; left: 142px; top: 42px; right: 0; padding-bottom: 10px; border-bottom: 1px solid var(--rule); }
  .card-back .person .name { font-size: 8px; font-weight: 700; color: var(--navy); }
  .card-back .person .title { font-size: 5.5px; color: var(--muted); margin-top: 1px; }
  .card-back .channels { position: absolute; left: 142px; top: 94px; font-size: 5.8px; line-height: 8.5px; color: var(--muted); }
  .card-back .contact-row svg { width: 5.5px; height: 5.5px; }
  .card-back .bottom-band { position: absolute; left: 0; bottom: 0; width: 100%; height: 6px; background: var(--navy); }
</style>
</head>
<body>

<section class="letterhead">
  <div class="lh-brand">
    <span class="brand-dot"></span>
    <span class="brand-name"><span class="line1">HARROWFIELD</span><span class="line2">PROPERTY PARTNERS</span></span>
  </div>

  <div class="lh-contact">
    <div class="address">418 Meridian Ave, Suite 900<br>Lakeport, FL 33190</div>
    <div class="channels">
      <div class="contact-row"><svg viewBox="0 0 16 16"><path d="M3 1l3 3-2 2c1 2 4 5 6 6l2-2 3 3-2 2C7 15 1 9 1 3z"/></svg>(555) 014-2290</div>
      <div class="contact-row"><svg viewBox="0 0 16 16"><path d="M1 3h14v10H1z M2 4l6 5 6-5" stroke="#fff" stroke-width="1.2"/></svg>dorsay@hrwpp-example.com</div>
    </div>
  </div>

  <div class="letter">
    <p class="date">July 30, 2020</p>
    <p class="salutation">Dear Mr. Carver,</p>
    <p class="body">Lorem ipsum dolor sit amet, consectetur adipiscing elit. Integer diam quam, egestas eu ultrices eu, suscipit ac sapien. Phasellus eu dui nisi. Nam et euismod diam, nec lobortis tortor. Donec et diam nulla. Aenean varius tincidunt convallis. Aliquam a tortor at lacus dictum aliquet. Nunc laoreet metus sapien, in scelerisque augue consectetur in.</p>
    <p class="body">Fusce nec justo laoreet, egestas justo sed, aliquet sem. Pellentesque pharetra massa non orci bibendum semper. Pellentesque cursus eu lectus a consectetur. Nunc volutpat suscipit posuere. Vestibulum facilisis vel quam malesuada mattis. Nulla in mattis tellus. Maecenas tristique mauris vitae pharetra tincidunt. In ut ornare risus. Integer molestie vestibulum nisi, semper dapibus mi condimentum eu.</p>
    <p class="body">Nullam sagittis elit libero, id fringilla est tincidunt eget. Donec in ipsum ultricies, consectetur quam vel, facilisis elit. Phasellus tincidunt congue risus vel luctus. Suspendisse ut mollis neque. Donec ornare orci in turpis vestibulum, in ultrices metus scelerisque. Pellentesque mattis mattis nunc, nec tincidunt lacus egestas id. Fusce facilisis sagittis neque sit amet vulputate. Aliquam ut eros lobortis tortor facilisis vehicula. Sed sed luctus leo, at laoreet sapien. Donec placerat adipiscing ligula non euismod. In lobortis pretium nisl id luctus.</p>
    <p class="body">Integer gravida tincidunt nibh, scelerisque tincidunt turpis. Suspendisse potenti. Nunc hendrerit euismod lectus id elementum. Fusce vitae gravida velit, quis eleifend lectus. In imperdiet mauris eu dui viverra sagittis. Donec tempor dui diam, condimentum gravida lacus pretium a. Nullam fringilla augue quis arcu placerat scelerisque. Aliquam nec tincidunt augue, sit amet posuere ipsum.</p>
    <p class="closing">Sincerely Yours,</p>
    <span class="signature" role="img" aria-label="Handwritten signature of Daniel Orsay"></span>
    <p>Daniel Orsay<br>Managing Partner Multifamily</p>
  </div>

  <footer class="lh-footer">www.hrwpp-example.com</footer>
</section>

<section class="card-front">
  <div class="brand">
    <span class="line1">HARROWFIELD</span>
    <span class="line2">PROPERTY PARTNERS</span>
    <span class="url">www.hrwpp-example.com</span>
  </div>
</section>

<section class="card-back">
  <div class="brand">
    <span class="brand-dot"></span>
    <span class="line1">HARROWFIELD</span>
    <span class="line2">PROPERTY PARTNERS</span>
  </div>
  <div class="address">418 Meridian Ave, Suite 900<br>Lakeport, FL 33190</div>
  <div class="person">
    <div class="name">Daniel Orsay</div>
    <div class="title">Managing Partner Multifamily</div>
  </div>
  <div class="channels">
    <div class="contact-row"><svg viewBox="0 0 16 16"><path d="M4 0h8v16H4z M6 2v11h4V2z"/></svg>(555) 014-2290</div>
    <div class="contact-row"><svg viewBox="0 0 16 16"><path d="M3 1l3 3-2 2c1 2 4 5 6 6l2-2 3 3-2 2C7 15 1 9 1 3z"/></svg>(555) 014-2291</div>
    <div class="contact-row"><svg viewBox="0 0 16 16"><path d="M1 3h14v10H1z"/></svg>dorsay@hrwpp-example.com</div>
    <div class="contact-row"><svg viewBox="0 0 16 16"><circle cx="8" cy="8" r="7"/></svg>www.hrwpp-example.com</div>
  </div>
  <div class="bottom-band"></div>
</section>

</body>
</html>
```